Company producing high tech raw materials for the bakery industry needs new packaging design

We need a new design for the bag containing our products.

We are a producer of chemical and high tech raw materials for the bakery and confectionery sectors (we have small customers & also large industrial customers).

Our profile is in between food and pharmaceuticals. So the new design needs to present foremostly seriousness and reliability, but still not being blunt and boring as it contains exciting cutting edge food technology ingredients.

We have 3 different sizes of bags to contain our products, (which is in the form of powder like flour). 650x400x130 for 10 kgs, 700x460x130 for 15 kgs, 900x500x130 for 25 kgs, so the design should look good in all three sizes. Bags are from thick paper.

I am attaching pictures of our current (very badly designed blue-grey) bag and some pictures of competition bags, so that you get an idea of how the bags in the industry generally are.

The new bag should contain the logo (attached). The colors used in the logo are CMYK , DARK BLUE 100,83,5,27 LIGHT BLUE 60,40,0,0. Our primary colors are like the ones in the logo and as secondary we have grey and yellow (orange). Maximum number of different colors that can be used in the new design is 4 (because the printing cost is much more expensive with more than that).

FYI on the bag, as you can see in the attached pictures of our current bag, must be an A5 - A4 size label and the top opening is sewed.

Please do not hesitate to contact us for any further questions or clarification.

Requirements
Must have
• Take into account the label and the closing on top of the bag
3 bag sizes
Highly visible logo

```html
<!DOCTYPE html>
<html lang="en">
<head>
<meta charset="utf-8">
<title>Velmora bag fronts, 10 kg</title>
<link rel="stylesheet" href="https://fonts.googleapis.com/css2?family=Questrial&family=Open+Sans:wght@700&display=swap">
<style>
  :root {
    --page: #ffffff;
    --bag-dark: #05050a;
    --bag-navy: #1f2433;
    --bag-grey: #47464d;
    --frame-blue: #6f8cc9;
    --label-bg: #e4e5e8;
    --brand-dark: #0f3178;
    --brand-light: #7088c8;
    --weight-white: #ffffff;
    --weight-grey: rgba(170, 170, 172, 0.9);
  }
  * { box-sizing: border-box; margin: 0; padding: 0; }
  html, body { width: 1200px; height: 1000px; overflow: hidden; background: var(--page); }
  .canvas { position: relative; width: 1200px; height: 1000px; }

  .bag {
    position: absolute; top: 95px; width: 498px; height: 810px;
    border: 1px solid #111;
    overflow: hidden;
  }
  .bag--small-label { left: 87px; }
  .bag--wide-label { left: 613px; width: 500px; }

  .bag__texture {
    position: absolute; inset: 0;
    background:
      radial-gradient(ellipse 60% 40% at 20% 15%, rgba(70,78,105,0.35), transparent 70%),
      radial-gradient(ellipse 50% 35% at 30% 70%, rgba(60,68,95,0.35), transparent 70%),
      linear-gradient(135deg, var(--bag-navy) 0%, var(--bag-dark) 45%, #101018 70%, var(--bag-grey) 100%);
  }

  .bag__frame {
    position: absolute; left: 12px; top: 11px; right: 12px; bottom: 11px;
    border: 1px solid var(--frame-blue);
    outline: 1px solid var(--frame-blue);
    outline-offset: -8px;
  }

  .label {
    position: absolute; background: var(--label-bg); border-radius: 12px;
    box-shadow: 0 4px 10px rgba(0,0,0,0.35);
    font-family: "Questrial", sans-serif;
  }
  .label__mark { position: absolute; border-radius: 50%; background: var(--brand-light); }
  .label__name { position: absolute; color: var(--brand-dark); line-height: 1; letter-spacing: -1px; }
  .label__sub { position: absolute; color: var(--brand-light); line-height: 1; letter-spacing: 2px; }

  .bag--small-label .label { left: 90px; top: 87px; width: 339px; height: 235px; }
  .bag--small-label .label__mark { left: 139px; top: 28px; width: 62px; height: 62px; }
  .bag--small-label .label__name { left: 0; right: 0; top: 122px; text-align: center; font-size: 66px; }
  .bag--small-label .label__sub { left: 0; right: 0; top: 196px; text-align: center; font-size: 22px; }

  .bag--wide-label .label { left: 41px; top: 87px; width: 416px; height: 111px; }
  .bag--wide-label .label__mark { left: 60px; top: 27px; width: 56px; height: 56px; }
  .bag--wide-label .label__name { left: 180px; top: 26px; font-size: 55px; }
  .bag--wide-label .label__sub { left: 183px; top: 80px; font-size: 16px; }

  .weight { position: absolute; font-family: "Open Sans", sans-serif; font-weight: 700; line-height: 1; white-space: nowrap; }
  .bag--small-label .weight { right: 46px; top: 695px; font-size: 72px; color: var(--weight-white); letter-spacing: -3px; }
  .bag--wide-label .weight { left: 33px; top: 284px; font-size: 180px; color: var(--weight-grey); letter-spacing: -10px; }
</style>
</head>
<body>
<main class="canvas">
  <section class="bag bag--small-label">
    <div class="bag__texture" role="img" aria-label="Dark marbled swirl texture in black, navy and grey"></div>
    <div class="bag__frame" role="img" aria-label="Fine light blue chain border"></div>
    <div class="label">
      <span class="label__mark"></span>
      <span class="label__name">Velmora</span>
      <span class="label__sub">ΑΦΟΙ ΚΑΛΛΙΔΗ</span>
    </div>
    <p class="weight">10 Kg</p>
  </section>

  <section class="bag bag--wide-label">
    <div class="bag__texture" role="img" aria-label="Dark marbled swirl texture in black, navy and grey"></div>
    <div class="bag__frame" role="img" aria-label="Fine light blue chain border"></div>
    <div class="label">
      <span class="label__mark"></span>
      <span class="label__name">Velmora</span>
      <span class="label__sub">ΑΦΟΙ ΚΑΛΛΙΔΗ</span>
    </div>
    <p class="weight">10 Kg</p>
  </section>
</main>
</body>
</html>
```